Redesign cement bags for leading cement producer in south east asia

We are from Talvero cement and would like to redesign our bag to relaunch the product line. Our bags are made of high quality PP woven sack. We are one of the leading cement producers and we want our bags to have a Talvero classy look on each visible side when it is loading in a truck or stacking on a pallet.

Thank you for interesting in this project. Good luck.
Updates

Project Deadline Extended Reason: Hi all, I have received requests to extend the deadline. Some of the work requires revising and some of them are still on process. To be fair, I also raise my budget to compensate the time. Thanks all for your participation. Added Sunday, July 10, 2016

Target Market(s)

Construction

Industry/Entity Type

Cement

Requirements
Must have
• You will have to design two bags for two cement grades. 52.5 is of higher grade and 42.5 is of lower grade. Both are similar in design but a distinctive colours to differentiate the two at once. Please look at Reference picture 2 for ideas.
Nice to have
• You do not have to change the original logo but the Talvero cement word font changes are required. There are no restrictions to colours and font but please refrain from using feminine colours. Instructions on rear side of the bags are now included in the scope. Please create new layout and design new user friendly symbols.
Should not have
• Since cement is a dusty product, you need avoid some colours like black as background. The dust need to be less obvious to attract attention. Our previous base colour are shown in below.
• We want a fresh look on our bag, please do not just copy our old design and make small changes. I have attached our competitors' design, please refrain from using their design as well.
• It is recommend to do some research on cement bag sector.

```html
<!DOCTYPE html>
<html lang="en">
<head>
<meta charset="utf-8">
<title>Talvero Cement – Bag Designs</title>
<link rel="stylesheet" href="https://fonts.googleapis.com/css2?family=Fjalla+One&family=Montserrat:wght@700;800&family=Roboto+Condensed:wght@500;700&display=swap">
<style>
  :root {
    --page: #ffffff;
    --kraft: #e7d3a7;
    --kraft-text: #ead5a4;
    --gold: #e2c27e;
    --blue-deep: #1f398c;
    --blue-bright: #0d7fc6;
    --red-deep: #b4141d;
    --red-bright: #e81a2e;
  }
  * { margin: 0; padding: 0; box-sizing: border-box; }
  html, body { width: 1200px; height: 1200px; overflow: hidden; background: var(--page); }
  .canvas { position: relative; width: 1200px; height: 1200px; }

  .bag {
    position: absolute; top: 212px; width: 528px; height: 776px;
    border-radius: 6px; overflow: hidden;
  }
  .bag--grade-425 { left: 50px; --deep: var(--blue-deep); --bright: var(--blue-bright); }
  .bag--grade-525 { left: 620px; --deep: var(--red-deep); --bright: var(--red-bright); }

  .bag__art { position: absolute; inset: 0; width: 100%; height: 100%; }
  .bag__art .deep { fill: var(--deep); }
  .bag__art .bright { fill: var(--bright); }
  .bag__art .kraft { fill: var(--kraft); }
  .bag__art .gold { fill: var(--gold); }

  .brand-name {
    position: absolute; top: 122px; left: 0; right: 0; text-align: center;
    font-family: "Fjalla One", "Arial Narrow", sans-serif; font-weight: 400; font-size: 92px; line-height: 1;
    color: var(--kraft-text); letter-spacing: 1px;
  }
  .brand-dot {
    position: absolute; top: 250px; left: 248px; width: 32px; height: 32px;
    border-radius: 50%; background: var(--kraft-text);
  }

  .product-type {
    position: absolute; top: 414px; left: 0; right: 0; text-align: center;
    font-family: "Montserrat", sans-serif; font-weight: 800; font-size: 30px; line-height: 1;
    color: var(--deep); letter-spacing: 0.5px;
  }
  .product-sub {
    position: absolute; top: 461px; left: 0; right: 0; text-align: center;
    font-family: "Montserrat", sans-serif; font-weight: 700; font-size: 17px; line-height: 1;
    color: var(--deep); letter-spacing: 7px; padding-left: 7px;
  }

  .spec {
    position: absolute; left: 103px; top: 508px;
    font-family: "Roboto Condensed", "Arial Narrow", sans-serif; font-weight: 500;
    font-size: 19px; line-height: 27px; color: var(--deep);
  }
  .weight {
    position: absolute; left: 103px; top: 574px; display: flex; align-items: center;
    color: var(--deep); font-family: "Roboto Condensed", sans-serif;
  }
  .weight__icon { display: flex; flex-direction: column; align-items: center; width: 36px; }
  .weight__pict { width: 22px; height: 20px; background: var(--deep); border-radius: 2px; }
  .weight__label { font-size: 9px; font-weight: 700; margin-top: 2px; }
  .weight__value {
    font-weight: 700; font-size: 28px; line-height: 1;
    border-left: 2px solid var(--deep); padding-left: 6px; margin-left: 4px; height: 38px;
    display: flex; align-items: center;
  }

  .uses {
    position: absolute; left: 337px; top: 512px;
    display: grid; grid-template-columns: 40px 40px; column-gap: 9px; row-gap: 5px;
  }
  .use { display: flex; flex-direction: column; align-items: center; }
  .use__pict { width: 39px; height: 39px; border: 2px solid var(--deep); border-radius: 3px;
    background: linear-gradient(135deg, var(--kraft) 0%, var(--deep) 100%); }
  .use__label {
    font-family: "Roboto Condensed", sans-serif; font-weight: 700; font-size: 8.5px;
    color: var(--deep); margin-top: 3px; line-height: 1;
  }

  .origin {
    position: absolute; top: 676px; left: 0; right: 0; text-align: center;
    font-family: "Montserrat", sans-serif; font-weight: 700; font-size: 13px;
    color: var(--gold); letter-spacing: 0.5px;
  }
</style>
</head>
<body>
<main class="canvas">

  <section class="bag bag--grade-425" aria-label="Talvero cement bag, strength class 42.5">
    <svg class="bag__art" viewBox="0 0 528 776" aria-hidden="true">
      <rect class="deep" width="528" height="776"/>
      <path class="bright" d="M0 292 H170 Q196 292 206 318 L212 330 H200 Q190 306 168 304 H0Z"/>
      <path class="bright" d="M0 316 H164 Q186 316 194 340 L200 352 H188 Q180 330 160 328 H0Z"/>
      <path class="bright" d="M0 340 H156 Q176 340 184 362 L188 372 H176 Q170 354 152 352 H0Z"/>
      <path class="bright" d="M528 292 H358 Q332 292 322 318 L316 330 H328 Q338 306 360 304 H528Z"/>
      <path class="bright" d="M528 316 H364 Q342 316 334 340 L328 352 H340 Q348 330 368 328 H528Z"/>
      <path class="bright" d="M528 340 H372 Q352 340 344 362 L340 372 H352 Q358 354 376 352 H528Z"/>
      <path class="kraft" d="M0 372 H180 Q200 372 214 388 H314 Q328 372 348 372 H528 V648 H0Z"/>
      <rect class="bright" y="648" width="528" height="8"/>
      <rect class="gold" y="662" width="528" height="2"/>
    </svg>
    <h1 class="brand-name">TALVERO</h1>
    <span class="brand-dot" aria-hidden="true"></span>
    <p class="product-type">CEMENT</p>
    <p class="product-sub">PORTLAND CEMENT</p>
    <p class="spec">Strength Class 42.5<br>EN 197-1:2000</p>
    <div class="weight">
      <div class="weight__icon"><span class="weight__pict" role="img" aria-label="Person lifting heavy bag pictogram"></span><span class="weight__label">HEAVY</span></div>
      <span class="weight__value">50kg</span>
    </div>
    <div class="uses">
      <div class="use"><span class="use__pict" role="img" aria-label="Concrete use pictogram"></span><span class="use__label">CONCRETE</span></div>
      <div class="use"><span class="use__pict" role="img" aria-label="Mortar use pictogram"></span><span class="use__label">MORTAL</span></div>
      <div class="use"><span class="use__pict" role="img" aria-label="Render use pictogram"></span><span class="use__label">RENDER</span></div>
      <div class="use"><span class="use__pict" role="img" aria-label="Grout use pictogram"></span><span class="use__label">GROUT</span></div>
    </div>
    <p class="origin">PRODUCT OF MYANMAR</p>
  </section>

  <section class="bag bag--grade-525" aria-label="Talvero cement bag, strength class 52.5">
    <svg class="bag__art" viewBox="0 0 528 776" aria-hidden="true">
      <rect class="deep" width="528" height="776"/>
      <path class="bright" d="M0 292 H170 Q196 292 206 318 L212 330 H200 Q190 306 168 304 H0Z"/>
      <path class="bright" d="M0 316 H164 Q186 316 194 340 L200 352 H188 Q180 330 160 328 H0Z"/>
      <path class="bright" d="M0 340 H156 Q176 340 184 362 L188 372 H176 Q170 354 152 352 H0Z"/>
      <path class="bright" d="M528 292 H358 Q332 292 322 318 L316 330 H328 Q338 306 360 304 H528Z"/>
      <path class="bright" d="M528 316 H364 Q342 316 334 340 L328 352 H340 Q348 330 368 328 H528Z"/>
      <path class="bright" d="M528 340 H372 Q352 340 344 362 L340 372 H352 Q358 354 376 352 H528Z"/>
      <path class="kraft" d="M0 372 H180 Q200 372 214 388 H314 Q328 372 348 372 H528 V648 H0Z"/>
      <rect class="bright" y="648" width="528" height="8"/>
      <rect class="gold" y="662" width="528" height="2"/>
    </svg>
    <h2 class="brand-name">TALVERO</h2>
    <span class="brand-dot" aria-hidden="true"></span>
    <p class="product-type">CEMENT</p>
    <p class="product-sub">PORTLAND CEMENT</p>
    <p class="spec">Strength Class 52.5<br>EN 197-1:2000</p>
    <div class="weight">
      <div class="weight__icon"><span class="weight__pict" role="img" aria-label="Person lifting heavy bag pictogram"></span><span class="weight__label">HEAVY</span></div>
      <span class="weight__value">50kg</span>
    </div>
    <div class="uses">
      <div class="use"><span class="use__pict" role="img" aria-label="Concrete use pictogram"></span><span class="use__label">CONCRETE</span></div>
      <div class="use"><span class="use__pict" role="img" aria-label="Mortar use pictogram"></span><span class="use__label">MORTAL</span></div>
      <div class="use"><span class="use__pict" role="img" aria-label="Render use pictogram"></span><span class="use__label">RENDER</span></div>
      <div class="use"><span class="use__pict" role="img" aria-label="Grout use pictogram"></span><span class="use__label">GROUT</span></div>
    </div>
    <p class="origin">PRODUCT OF MYANMAR</p>
  </section>

</main>
</body>
</html>
```